Signage Design Project

i need to design a signage to be place at the fencing for a development. i want it to be simple and eye catching

Industry/Entity Type

Fencing

```html
<!DOCTYPE html>
<html lang="en">
<head>
<meta charset="UTF-8">
<title>Commercial Spaces – Coming Soon Sign</title>
<link rel="stylesheet" href="https://fonts.googleapis.com/css2?family=Cabin:wght@700&family=Oswald:wght@700&display=swap">
<style>
  :root {
    --sky: #00a9e6;
    --shadow: #005e80;
    --post: #ffffff;
    --panel-top: #fcdc00;
    --panel-side: #f4b400;
    --panel-core: #e8821e;
    --ink: #231f20;
    --light: #ffffff;
  }
  * { margin: 0; padding: 0; box-sizing: border-box; }
  html, body { width: 1200px; height: 1000px; overflow: hidden; background: var(--sky); }
  .canvas { position: relative; width: 1200px; height: 1000px; background: var(--sky); }
  .scene { position: absolute; inset: 0; }
  .eyebrow {
    position: absolute; left: 273px; width: 655px; top: 176px; text-align: center;
    font-family: "Cabin", sans-serif; font-weight: 700; font-size: 44px; line-height: 1;
    letter-spacing: 0.5px; color: var(--ink);
  }
  .headline {
    position: absolute; left: 377px; width: 452px; top: 327px; text-align: center;
    font-family: "Oswald", sans-serif; font-weight: 700; font-size: 61px; line-height: 80px;
    letter-spacing: 0.5px; color: var(--ink);
  }
  .usage { position: absolute; left: 388px; width: 452px; text-align: center; font-family: "Cabin", sans-serif; font-weight: 700; }
  .suitable { top: 491px; font-size: 29px; line-height: 1; color: var(--light); }
  .uses { top: 522px; font-size: 33px; line-height: 32px; list-style: none; color: var(--ink); }
  .contact {
    position: absolute; left: 330px; top: 689px;
    font-family: "Cabin", sans-serif; font-weight: 700; font-size: 36px; line-height: 1;
    letter-spacing: 0.5px; color: var(--light);
  }
</style>
</head>
<body>
<div class="canvas">
  <svg class="scene" width="1200" height="1000" viewBox="0 0 1200 1000" aria-hidden="true">
    <defs>
      <filter id="soft-shadow" x="-20%" y="-50%" width="140%" height="200%">
        <feGaussianBlur stdDeviation="18"/>
      </filter>
    </defs>
    <path class="ground-shadow" d="M120 790 L990 790 L1010 900 L170 900 Z" fill="var(--shadow)" filter="url(#soft-shadow)"/>
    <rect class="post post-left" x="236" y="84" width="36" height="831" fill="var(--post)"/>
    <rect class="post post-right" x="928" y="84" width="38" height="831" fill="var(--post)"/>
    <g class="board">
      <rect class="board-core" x="273" y="122" width="655" height="630" fill="var(--panel-core)"/>
      <polygon class="bevel-top" points="273,122 928,122 810,290 388,290" fill="var(--panel-top)"/>
      <polygon class="bevel-left" points="273,122 388,290 388,585 273,750" fill="var(--panel-side)"/>
      <polygon class="bevel-right" points="928,122 810,290 810,585 928,750" fill="var(--panel-side)"/>
    </g>
    <line class="contact-rule" x1="497" y1="712" x2="878" y2="712" stroke="var(--ink)" stroke-width="4"/>
  </svg>

  <p class="eyebrow">Coming Soon</p>
  <h1 class="headline">COMMERCIAL<br>SPACES</h1>
  <p class="usage suitable">Suitable for</p>
  <ul class="usage uses">
    <li>SHOPS</li>
    <li>SHOWROOMS</li>
    <li>OFFICES</li>
  </ul>
  <p class="contact">CONTACT</p>
</div>
</body>
</html>
```